Vorental d.o.o. needes a web site design

We are a company dealing with automatic doors, industrial doors, roller shutters, access control systems.
We would like to get a design which is clean and neat, and here are some sites which work with similar products. These designs are some we like, but of course, I am looking for a design which is unique. We usually use grey and red colours, which you can see on www.vorental.ba .
The sites we like are:
http://www.plinsta.com/gb/
http://www.bravidosteel.it/eng/
http://morrowpanelgate.com/

You have to understand, that we have 4 different groups of products, which are main groups. I would like if those 4 groups somehow could be in different colours. (Maybe "zenpoq" colours), in order to separate the groups in some way.

Attached you have web site structure.

If any questions, please contact me.
Edvan

Target Market(s)

Bosnian market. Aluminium and PVC doors and window market, Construction companies, Supermarkets-Retail, Gas stations, Banks, Food industry, Heavy industry.

Industry/Entity Type

It Company

Contact Information for Business Card

I have attached our current business card in PDF. I weould like english on one side, bosnian on other side.

Logo Text

Vorental is the name of the company, our core business is automation!

Number of Pages Required

5+ page

Font styles to use
Sans Serif

Colors
ec1f27
0792cd
9bcb3c
ffc214
ffffff

```html
<!DOCTYPE html>
<html lang="bs">
<head>
<meta charset="utf-8">
<title>Vorental d.o.o.</title>
<link rel="stylesheet" href="https://fonts.googleapis.com/css2?family=Carlito:ital,wght@0,400;0,700;1,700&display=swap">
<style>
:root{
  --red:#ee1c24;
  --rose:#e5646c;
  --rose-soft:#e8969c;
  --grey-dark:#5a5a5a;
  --grey-box:#8a8a8a;
  --grey-footer:#c4c4c4;
  --white:#ffffff;
  --ink:#111111;
}
*{margin:0;padding:0;box-sizing:border-box}
html,body{width:1200px;height:960px;overflow:hidden;background:var(--white)}
body{position:relative;font-family:'Carlito',sans-serif;color:var(--ink)}
.brand{position:absolute;left:52px;top:46px;display:flex;align-items:center;gap:12px}
.brand-mark{width:26px;height:26px;background:var(--red)}
.brand-name{font-size:40px;font-weight:400;color:var(--grey-dark);letter-spacing:1px}
.search{position:absolute;left:883px;top:17px;width:254px;height:27px;background:var(--rose-soft);color:var(--white);font-size:15px;line-height:27px;padding-left:11px}
.nav{position:absolute;left:0;top:124px;width:1200px;height:28px;background:var(--rose);border-bottom:3px solid var(--white);box-shadow:0 3px 0 #9a9a9a}
.nav ul{list-style:none;position:absolute;left:261px;top:4px;display:flex;gap:26px}
.nav li{color:var(--white);font-size:15.5px}
.hero{position:absolute;left:0;top:169px;width:1200px;height:272px;background:linear-gradient(90deg,#d9d6d2 0%,#a7a19a 25%,#6b5a48 50%,#8b7660 70%,#c9c2b8 100%)}
.feature{position:absolute;left:0;top:385px;width:413px;height:239px;background:var(--white);border-top-right-radius:26px}
.feature-inner{position:absolute;left:0;top:8px;width:406px;height:231px;background:var(--red);border-top-right-radius:20px;padding:8px 11px;color:var(--white)}
.feature h1{font-size:32px;font-style:italic;font-weight:700;line-height:1.05;margin-bottom:4px}
.feature p{font-size:20.5px;line-height:27px}
.card{position:absolute;top:455px;width:298px;height:169px;background:var(--grey-box);border-top-right-radius:20px;padding:6px 10px;color:var(--white)}
.card h2{font-size:30px;font-style:italic;font-weight:700;line-height:1.05;margin-bottom:3px}
.card p{font-size:15px;line-height:20px}
.card-news{left:428px}
.card-refs{left:750px;top:457px}
.intro{position:absolute;left:136px;top:657px;width:928px;text-align:center;font-size:15px;line-height:20.5px}
.footer{position:absolute;left:0;top:776px;width:1200px;height:184px;background:var(--grey-footer);color:#f7f7f7;font-size:15px;line-height:20px}
.contact{position:absolute;left:40px;top:22px}
.contact dl{display:grid;grid-template-columns:26px auto}
.contact dt{font-weight:700;color:var(--white);text-align:center}
.contact .gap{margin-top:10px}
.legal{position:absolute;left:230px;top:52px;width:211px;text-align:right}
.quote{position:absolute;left:801px;top:19px;width:334px;height:77px;background:var(--rose);border:3px solid var(--white);border-radius:8px;box-shadow:0 3px 4px rgba(0,0,0,.3);color:var(--white);font-size:38px;font-style:italic;font-weight:700;text-align:center;line-height:70px}
.copyright{position:absolute;right:68px;top:152px}
</style>
</head>
<body>
<header>
  <div class="brand"><span class="brand-mark"></span><span class="brand-name">Vorental d.o.o.</span></div>
  <div class="search">Pretraga ovdje...</div>
  <nav class="nav"><ul>
    <li>Home</li><li>Automatska Vrata</li><li>Industrijska Vrata</li><li>Rolo Vrata</li><li>Kontrola Pristupa</li><li>Reference</li>
  </ul></nav>
</header>
<div class="hero" role="img" aria-label="Fotografija automatskih staklenih vrata na ulazu u trgovački centar"></div>
<section class="feature"><div class="feature-inner">
  <h1>AUTOMATSKA VRATA</h1>
  <p>Lorem ipsum dolor sit amet, consectetur adipiscing elit. Suspendisse dui augue, interdum ut malesuada non, ullamcorper non turpis. Class aptent taciti sociosqu ad litora torquent per conubia nostra, per inceptos himenaeos.</p>
</div></section>
<section class="card card-news">
  <h2>VIJESTI</h2>
  <p>Donec porta ac dui non cursus. Aliquam auctor blandit turpis, quis interdum lectus consequat id. Vivamus et ante vitae turpis gravida elementum. Donec vel arcu non velit semper fringilla.</p>
</section>
<section class="card card-refs">
  <h2>REFERENCE</h2>
  <p>In eu turpis dapibus, ultrices lacus sit amet, consequat enim. Ut a odio nisi. Mauris odio nisl, viverra non dignissim sit amet, efficitur nec tellus.</p>
</section>
<p class="intro">Lorem ipsum dolor sit amet, consectetur adipiscing elit. Suspendisse dui augue, interdum ut malesuada non, ullamcorper non turpis. Class aptent taciti sociosqu ad litora torquent per conubia nostra, per inceptos himenaeos. Donec porta ac dui non cursus. Aliquam auctor blandit turpis, quis interdum lectus consequat id. Vivamus et ante vitae turpis gravida elementum. Donec vel arcu non velit semper fringilla. Duis pretium felis at tempor auctor. Lorem ipsum dolor sit amet, consectetur adipiscing elit.</p>
<footer class="footer">
  <div class="contact"><dl>
    <dt>A</dt><dd>Lipova Brigada BB,<br>74000 DOBOJ</dd>
    <dt class="gap">T</dt><dd class="gap">053/417-220</dd>
    <dt>F</dt><dd>053/417-221</dd>
    <dt>M</dt><dd>066/382-914</dd>
    <dt>E</dt><dd>info@vorental.ba</dd>
  </dl></div>
  <div class="legal">PDV broj: 407162935518<br>ID broj: 4407162935518<br>Poslovna banka:<br>Savska Banka Doboj<br>178-032-004-2215-067</div>
  <div class="quote">Zatražiti Citat!</div>
  <div class="copyright">C 2008-2016- Vorental d.o.o Doboj</div>
</footer>
</body>
</html>
```